Home Care company needs letter head branding

Home care company needs a letter head which can be used for all documents the company's clients view. We provided in home care for the elderly. We would like to use our company colors (2785A7, 0A4057 and 34A74D) and should not be too large as we will be using it on more than just a letter head but all documents our clients sign / receive.
Target Market(s)
Professional business
Industry/Entity Type
Health Care
Requirements
Must have
- corporate brand colors

```html
<!DOCTYPE html>
<html lang="en">
<head>
<meta charset="utf-8">
<title>Oakhaven Care – Letterhead</title>
<link href="https://fonts.googleapis.com/css2?family=Open+Sans:wght@400;600&display=swap" rel="stylesheet">
<style>
  :root {
    --brand-teal: #2785a7;
    --brand-lime: #abcd37;
    --ink: #1f1f1f;
    --paper: #f8f8f8;
    --watermark: #e9e7e7;
    --divider: #9a9a9a;
    --backdrop: #d6d6d6;
    --white: #ffffff;
  }
  * { box-sizing: border-box; margin: 0; padding: 0; }
  html, body {
    width: 1200px;
    height: 1200px;
    overflow: hidden;
    background: var(--backdrop);
    font-family: "Open Sans", sans-serif;
  }
  .letterhead {
    position: absolute;
    left: 233px;
    top: 50px;
    width: 734px;
    height: 1100px;
    background: var(--paper);
    overflow: hidden;
    box-shadow: 0 6px 18px rgba(0,0,0,0.25);
  }
  .brand {
    position: absolute;
    left: 54px;
    top: 52px;
    display: flex;
    align-items: center;
    gap: 12px;
  }
  .brand-mark {
    width: 72px;
    height: 72px;
    border-radius: 50%;
    background: var(--brand-teal);
  }
  .brand-name {
    font-size: 36px;
    font-weight: 600;
    color: var(--brand-teal);
    letter-spacing: -0.3px;
  }
  .header-divider {
    position: absolute;
    left: 460px;
    top: 43px;
    width: 1px;
    height: 84px;
    background: var(--divider);
  }
  .contact-list {
    position: absolute;
    right: 26px;
    top: 50px;
    list-style: none;
    text-align: right;
    font-size: 18px;
    line-height: 23.5px;
    color: var(--ink);
  }
  .contact-list li {
    display: flex;
    justify-content: flex-end;
    align-items: center;
    gap: 10px;
  }
  .contact-icon {
    width: 14px;
    height: 14px;
    fill: var(--brand-teal);
    flex: none;
  }
  .watermark {
    position: absolute;
    left: 37px;
    top: 212px;
    width: 696px;
    height: 696px;
    border-radius: 50%;
    background: var(--watermark);
    opacity: 0.75;
  }
  .footer-wave {
    position: absolute;
    left: 0;
    bottom: 0;
    width: 734px;
    height: 133px;
    display: block;
  }
  .footer-address {
    position: absolute;
    right: 40px;
    bottom: 27px;
    text-align: right;
    font-size: 18px;
    line-height: 23px;
    color: var(--white);
  }
</style>
</head>
<body>
  <main class="letterhead">
    <header>
      <div class="brand">
        <span class="brand-mark"></span>
        <span class="brand-name">Oakhaven Care</span>
      </div>
      <div class="header-divider"></div>
      <ul class="contact-list">
        <li>044-123 456 789
          <svg class="contact-icon" viewBox="0 0 24 24"><path d="M6.6 10.8a15.1 15.1 0 0 0 6.6 6.6l2.2-2.2a1 1 0 0 1 1-.25 11.4 11.4 0 0 0 3.6.57 1 1 0 0 1 1 1V20a1 1 0 0 1-1 1A17 17 0 0 1 3 4a1 1 0 0 1 1-1h3.5a1 1 0 0 1 1 1c0 1.25.2 2.45.57 3.57a1 1 0 0 1-.25 1z"/></svg>
        </li>
        <li>info@webname.com
          <svg class="contact-icon" viewBox="0 0 24 24"><path d="M2 5h20v14H2z"/><path d="M3 6l9 7 9-7" fill="none" stroke="#f8f8f8" stroke-width="2"/></svg>
        </li>
        <li>www.websitename.com
          <svg class="contact-icon" viewBox="0 0 24 24"><path d="M10 14a4 4 0 0 0 5.7 0l3.6-3.6a4 4 0 0 0-5.7-5.7l-1.3 1.3M14 10a4 4 0 0 0-5.7 0l-3.6 3.6a4 4 0 0 0 5.7 5.7l1.3-1.3" fill="none" stroke="#2785a7" stroke-width="2.4" stroke-linecap="round"/></svg>
        </li>
      </ul>
    </header>

    <div class="watermark" role="img" aria-label="Large faint brand emblem area"></div>

    <footer>
      <svg class="footer-wave" viewBox="0 860 653 118" preserveAspectRatio="none">
        <path d="M0 865 C100 930 250 945 390 912 C250 948 100 952 0 905 Z" fill="var(--brand-lime)"/>
        <path d="M0 908 C120 955 260 960 390 912 C480 888 580 885 653 898 L653 978 L0 978 Z" fill="var(--brand-teal)"/>
        <path d="M0 906 C120 953 260 958 390 910" fill="none" stroke="var(--white)" stroke-width="2"/>
      </svg>
      <address class="footer-address" style="font-style: normal;">
        12345, Address Goes Here<br>
        Country Name, 123456.
      </address>
    </footer>
  </main>
</body>
</html>
```